K7 Digital Stationery Design Project

We are looking to have stationary designs created for our company branding materials. We are looking for the following to be created.
1. Business Cards (front & back)
2. Letterhead
3. Envelopes #10
We are a new web design, development and marketing firm. Primary color scheme is desired to be blue/grey/white. This web start-up is owned and operated by individuals with 15+ years experience each in the industry so should not look as though it is a start-up by young/inexperienced individuals.
We build website & custom applications/software. In addition we provide the full spectrum of web marketing solutions including SEO, PPC, Social Media, Branding, Content Marketing and PR.
Please let us know if you have any questions. Looking forward to seeing all the amazing design ideas.
Attached is our logo.
Thanks!
Target Market(s)
Company will be nearly 100% business to business sales. Looking to work with companies that are already established, with a website, who want to take their website and/or online marketing efforts to the next level.
Industry/Entity Type
Marketing
Look and feel

```html
<!DOCTYPE html>
<html lang="en">
<head>
<meta charset="utf-8">
<title>K7 Digital Stationery</title>
<link href="https://fonts.googleapis.com/css2?family=Jost:wght@600&family=Arimo:wght@400;700&display=swap" rel="stylesheet">
<style>
  :root {
    --ink: #000000;
    --paper: #ffffff;
    --blue-light: #00b0db;
    --blue-mid: #1a9ad6;
    --blue-deep: #1473c1;
    --mark-grey: #dcdddf;
    --rule-grey: #9a9a9a;
    --text-grey: #5a5a5a;
  }
  html, body {
    margin: 0;
    padding: 0;
    width: 1200px;
    height: 721px;
    overflow: hidden;
    background: var(--ink);
  }
  .canvas {
    position: relative;
    width: 1200px;
    height: 721px;
    background: var(--ink);
    font-family: "Arimo", Arial, sans-serif;
  }
  .sheet {
    position: absolute;
    background: var(--paper);
    overflow: hidden;
  }
  .brand {
    position: absolute;
    font-family: "Jost", "Futura", sans-serif;
    font-weight: 600;
    white-space: nowrap;
    line-height: 1;
  }
  .brand-name { display: block; letter-spacing: -0.2px; }
  .brand-tagline {
    display: block;
    font-size: 0.42em;
    letter-spacing: 0;
    margin-top: 2px;
  }
  .decor-circle {
    position: absolute;
    border-radius: 50%;
    background: var(--mark-grey);
  }
  .contact {
    position: absolute;
    color: var(--text-grey);
    font-size: 6.4px;
    line-height: 7.4px;
    white-space: nowrap;
  }
  .rule-v {
    position: absolute;
    width: 1px;
    background: var(--rule-grey);
  }

  /* Letterhead */
  .letterhead { left: 46px; top: 40px; width: 504px; height: 650px; }
  .letterhead-header {
    position: absolute; left: 0; top: 0; width: 100%; height: 101px;
    background: linear-gradient(90deg, var(--blue-deep) 0%, var(--blue-mid) 55%, var(--blue-light) 100%);
  }
  .letterhead .brand { right: 30px; top: 74px; color: var(--paper); font-size: 13px; text-align: right; }
  .letterhead .decor-circle { width: 230px; height: 230px; left: 395px; top: 455px; }
  .letterhead .rule-v { left: 391px; top: 596px; height: 49px; }
  .letterhead .contact { left: 402px; top: 597px; }
  .letterhead-footer {
    position: absolute; left: 0; bottom: 0; width: 100%; height: 6px;
    background: linear-gradient(90deg, var(--blue-light), var(--blue-deep));
  }

  /* Business cards */
  .card { top: 29px; width: 208px; height: 118px; border-radius: 14px; }
  .card-front { left: 577px; }
  .card-front .decor-circle { width: 120px; height: 120px; left: 140px; top: -10px; }
  .card-front .edge-blue {
    position: absolute; left: 0; top: 45px; width: 5px; height: 29px; background: var(--blue-mid);
  }
  .card-front .edge-grey {
    position: absolute; right: 0; top: 45px; width: 5px; height: 29px; background: #555;
  }
  .card-front .brand { right: 105px; top: 44px; color: var(--blue-deep); font-size: 8.5px; text-align: right; transform: translateX(100%); }
  .card-front .holder {
    position: absolute; right: 105px; top: 63px; text-align: right; color: var(--text-grey);
  }
  .holder-name { font-weight: 700; font-size: 6.6px; display: block; color: #444; }
  .holder-role { font-size: 4.6px; display: block; margin-top: 1px; }
  .card-front .contact { right: 105px; top: 82px; font-size: 4.4px; line-height: 5.4px; text-align: right; }
  .card-front .rule-h {
    position: absolute; left: 105px; top: 106px; width: 96px; height: 1px; background: var(--rule-grey);
  }
  .card-back {
    left: 797px;
    background: linear-gradient(135deg, var(--blue-light) 0%, var(--blue-mid) 50%, var(--blue-deep) 100%);
  }
  .card-back .decor-circle { width: 110px; height: 110px; left: 130px; top: -20px; background: rgba(20, 115, 193, 0.55); }
  .card-back .brand { left: 72px; top: 66px; color: var(--paper); font-size: 8.5px; text-align: center; }

  /* Envelope back (flap side with return address) */
  .envelope-back { left: 576px; top: 169px; width: 593px; height: 249px; }
  .envelope-back .decor-circle { width: 200px; height: 200px; left: 470px; top: 30px; }
  .envelope-back .brand { left: 25px; top: 203px; color: var(--blue-deep); font-size: 10px; }
  .envelope-back .rule-v { left: 114px; top: 205px; height: 44px; }
  .envelope-back .contact { left: 124px; top: 204px; font-size: 4.8px; line-height: 5.6px; }

  /* Envelope front */
  .envelope-front { left: 576px; top: 441px; width: 593px; height: 249px; }
  .envelope-front .blue-panel { position: absolute; left: 0; top: 0; width: 593px; height: 249px; }
  .envelope-front .panel-dot {
    position: absolute; left: 566px; top: 112px; width: 12px; height: 12px; border-radius: 50%; background: var(--paper);
  }
</style>
</head>
<body>
<div class="canvas">

  <section class="sheet letterhead" aria-label="Letterhead">
    <div class="letterhead-header"></div>
    <div class="brand">
      <span class="brand-name">K7 DIGITAL</span>
      <span class="brand-tagline">Web Design, Development and Marketing</span>
    </div>
    <div class="decor-circle"></div>
    <div class="rule-v"></div>
    <address class="contact" style="font-style:normal">
      123 street, City &amp; Country<br>
      Phone :&nbsp; 88 123 123 123<br>
      Cell : 88 123 123 123<br>
      Fax : 88 123 123 123<br>
      info@k7digital.com
    </address>
    <div class="letterhead-footer"></div>
  </section>

  <section class="sheet card card-front" aria-label="Business card front">
    <div class="decor-circle"></div>
    <div class="edge-blue"></div>
    <div class="edge-grey"></div>
    <div class="brand" style="transform:none">
      <span class="brand-name">K7 DIGITAL</span>
      <span class="brand-tagline">Web Design, Development and Marketing</span>
    </div>
    <div class="holder">
      <span class="holder-name">Here your name</span>
      <span class="holder-role">Designation</span>
    </div>
    <address class="contact" style="font-style:normal">
      123 street, City &amp; Country<br>
      Phone :&nbsp; 88 123 123 123<br>
      Cell : 88 123 123 123<br>
      Fax : 88 123 123 123<br>
      info@k7digital.com
    </address>
    <div class="rule-h"></div>
  </section>

  <section class="sheet card card-back" aria-label="Business card back">
    <div class="decor-circle"></div>
    <div class="brand">
      <span class="brand-name">K7 DIGITAL</span>
      <span class="brand-tagline">Web Design, Development and Marketing</span>
    </div>
  </section>

  <section class="sheet envelope-back" aria-label="Envelope with return address">
    <div class="decor-circle"></div>
    <div class="brand">
      <span class="brand-name">K7 DIGITAL</span>
      <span class="brand-tagline">Web Design, Development and Marketing</span>
    </div>
    <div class="rule-v"></div>
    <address class="contact" style="font-style:normal">
      123 street, City &amp; Country<br>
      Phone :&nbsp; 88 123 123 123<br>
      Cell : 88 123 123 123<br>
      Fax : 88 123 123 123<br>
      info@k7digital.com
    </address>
  </section>

  <section class="sheet envelope-front" aria-label="Envelope front">
    <svg class="blue-panel" viewBox="0 0 593 249" width="593" height="249" aria-hidden="true">
      <defs>
        <linearGradient id="panelBlue" x1="0" y1="0" x2="0" y2="1">
          <stop offset="0" stop-color="#00b0db"/>
          <stop offset="1" stop-color="#1473c1"/>
        </linearGradient>
      </defs>
      <polygon points="553,0 593,0 593,249 554,249 534,127" fill="url(#panelBlue)"/>
    </svg>
    <div class="panel-dot"></div>
  </section>

</div>
</body>
</html>
```